Heavy Duty Electrical Plug Label Design

This electrical plug is unlike anything on the market today. It is 1 male electrical plug that can fit 9 DIFFERENT female receptacles. The most configurations plugs on the market have today is 2. This electrical plug is for heavy duty electricity that runs items such as welders and other big electrical equipment. I have a label I came up with but it is was done on word and you can tell. The label needs to highlight the transforming/configurations aspects of the plug, different combinations, and needs to communicate heavy duty. I am not set on the design I have. All of the configurations the label fits are in the label I uploaded. I will check this every day in case you have any questions. Thank you! Final size will be wrapped around device and label will be 3.75" tall and 8.5" wide.

Target Market(s)

Electricians and owners of heavy duty electrical equipment. Welders, big portable electric heaters, punch machines are a few items that can be put on the product

Industry/Entity Type

Electrical

Font styles to use
Sans Serif

Requirements
Must have
• Highlight different configurations and convey heavy duty.
Nice to have
• Red and black seem to be my running colors but I am open to creativity! A simple design seems to have a bold impact and get noticed. Competitor's plugs are not packaged well.

```html
<!DOCTYPE html>
<html lang="en">
<head>
<meta charset="utf-8">
<title>Omni-Plug Label</title>
<link rel="stylesheet" href="https://fonts.googleapis.com/css2?family=Anton&family=Montserrat:wght@300;400;500;600;700;800&display=swap">
<style>
  :root {
    --ink: #ffffff;
    --red: #e21d2f;
    --red-deep: #a8121f;
    --red-bright: #f0303f;
    --bg-dark: #0d0e10;
    --bg-mid: #3a3b3e;
    --silver-light: #f2f2f2;
    --silver-dark: #9a9a9a;
    --strip-dark: #1e1f21;
    --strip-mid: #4a4b4d;
    --outlet-line: #b9b9b9;
    --outlet-fill-top: #3a3b3d;
    --outlet-fill-bottom: #242527;
    --label-text: #1a1a1a;
  }
  * { margin: 0; padding: 0; box-sizing: border-box; }
  html, body { width: 1200px; height: 707px; overflow: hidden; background: var(--bg-dark); }
  body { font-family: "Montserrat", sans-serif; color: var(--ink); }

  .label {
    position: relative; width: 1200px; height: 707px; overflow: hidden;
    background: radial-gradient(ellipse 620px 300px at 620px 360px, var(--bg-mid) 0%, #1c1d20 60%, var(--bg-dark) 100%);
  }

  .company { position: absolute; left: 448px; top: 59px; font-size: 29px; font-weight: 600; line-height: 1.1; }

  .product-band {
    position: absolute; left: 426px; top: 103px; width: 774px; height: 131px;
    background: linear-gradient(100deg, var(--red-deep) 0%, var(--red) 30%, var(--red-bright) 45%, var(--red-deep) 65%, var(--red) 100%);
  }
  .product-name {
    position: absolute; left: 22px; top: 14px; font-family: "Anton", sans-serif;
    font-size: 100px; font-weight: 400; line-height: 1; color: var(--ink);
  }

  .ratings { position: absolute; left: 35px; top: 110px; font-size: 21px; line-height: 33px; }
  .ratings .value { color: var(--red); font-size: 27px; font-weight: 500; }

  .ratings-rule { position: absolute; left: 0; top: 230px; width: 420px; height: 3px; background: var(--red); }

  .steps { position: absolute; left: 42px; top: 262px; list-style: none; font-size: 17.5px; font-weight: 300; line-height: 27px; }

  .tagline { position: absolute; left: 451px; top: 252px; font-size: 31px; font-weight: 800; letter-spacing: -0.3px; }
  .tagline .dot { margin: 0 14px; }

  .config-tab {
    position: absolute; left: 692px; top: 402px; width: 508px; height: 50px;
    background: linear-gradient(90deg, var(--silver-dark) 0%, var(--silver-light) 35%, #d4d4d4 70%, var(--silver-light) 100%);
    clip-path: polygon(41px 0, 100% 0, 100% 100%, 0 100%);
  }
  .config-tab p {
    position: absolute; right: 31px; top: 9px; font-size: 24px; font-weight: 600; color: var(--label-text);
  }

  .outlet-strip {
    position: absolute; left: 0; top: 452px; width: 1200px; height: 174px;
    background: linear-gradient(180deg, var(--strip-dark) 0%, var(--strip-mid) 50%, var(--strip-dark) 100%);
    border-top: 1px solid #cfcfcf; border-bottom: 1px solid #cfcfcf;
  }
  .outlet { position: absolute; top: 27px; width: 91px; text-align: center; }
  .outlet-face {
    width: 91px; height: 107px; border: 1.5px solid var(--outlet-line); border-radius: 7px;
    background: linear-gradient(180deg, var(--outlet-fill-top), var(--outlet-fill-bottom));
  }
  .outlet span { display: block; margin-top: 5px; font-size: 17px; font-weight: 600; line-height: 1.2; }

  .patent { position: absolute; left: 53px; top: 645px; font-size: 17px; }
  .warning { position: absolute; left: 790px; top: 641px; font-size: 17px; line-height: 22px; display: flex; gap: 5px; }
  .warning svg { width: 26px; height: 24px; flex: none; }
  .warning strong { font-weight: 700; }
</style>
</head>
<body>
<div class="label">
  <p class="company">Harlow Company</p>
  <div class="product-band"><p class="product-name">Omni-Plug</p></div>

  <p class="ratings">Built for<br>
    <span class="value">30-60</span> Amperes<br>
    <span class="value">125/208/250</span> Volts</p>
  <div class="ratings-rule"></div>

  <ol class="steps">
    <li>1. Disconnect Electricity</li>
    <li>2. Loosen cord clamp</li>
    <li>3. Unscrew plug housing</li>
    <li>4. Change configuration</li>
    <li>5. Re-Assemble</li>
  </ol>

  <p class="tagline">HEAVY DUTY<span class="dot">•</span>TRANSFORMING</p>

  <div class="config-tab"><p>1 Plug &nbsp;|&nbsp; 9 Different Configuration</p></div>

  <div class="outlet-strip">
    <div class="outlet" style="left:54px"><div class="outlet-face" role="img" aria-label="14-30 receptacle face diagram"></div><span>14-30</span></div>
    <div class="outlet" style="left:179px"><div class="outlet-face" role="img" aria-label="14-50 receptacle face diagram"></div><span>14-50</span></div>
    <div class="outlet" style="left:304px"><div class="outlet-face" role="img" aria-label="14-60 receptacle face diagram"></div><span>14-60</span></div>
    <div class="outlet" style="left:429px"><div class="outlet-face" role="img" aria-label="15-30 receptacle face diagram"></div><span>15-30</span></div>
    <div class="outlet" style="left:554px"><div class="outlet-face" role="img" aria-label="15-50 receptacle face diagram"></div><span>15-50</span></div>
    <div class="outlet" style="left:679px"><div class="outlet-face" role="img" aria-label="15-60 receptacle face diagram"></div><span>15-60</span></div>
    <div class="outlet" style="left:804px"><div class="outlet-face" role="img" aria-label="18-30 receptacle face diagram"></div><span>18-30</span></div>
    <div class="outlet" style="left:929px"><div class="outlet-face" role="img" aria-label="18-50 receptacle face diagram"></div><span>18-50</span></div>
    <div class="outlet" style="left:1054px"><div class="outlet-face" role="img" aria-label="18-60 receptacle face diagram"></div><span>18-60</span></div>
  </div>

  <p class="patent">* Patent Pending</p>
  <div class="warning">
    <svg viewBox="0 0 26 24"><path d="M13 1 L25 23 H1 Z" fill="#fff"/><rect x="11.6" y="8" width="2.8" height="8" fill="#111"/><rect x="11.6" y="18" width="2.8" height="2.8" fill="#111"/></svg>
    <p><strong>WARNING:</strong> Read all instructions before<br>use to avoid injury, shock or damage.</p>
  </div>
</div>
</body>
</html>
```